Harold Vane Collective - Juvenile Skeletal Repair Agenda Framing Network

A 2-sided A4 leaflet to explain the research priorities in Children's Orthopaedic Surgery.
We would like this to be similar to that produced previously by the physiotherapists.

```html
<!DOCTYPE html>
<html lang="en">
<head>
<meta charset="utf-8">
<title>Harold Vane Collective – Top 10 research priorities</title>
<link rel="stylesheet" href="https://fonts.googleapis.com/css2?family=Nunito:wght@900&family=Arimo:wght@400;500;700&display=swap">
<style>
  :root {
    --orange: #F5B120;
    --lime: #D6D623;
    --sage: #A4CABC;
    --teal: #0093A0;
    --teal-text: #0E8F9C;
    --navy: #24246B;
    --white: #ffffff;
  }
  * { margin: 0; padding: 0; box-sizing: border-box; }
  html, body { width: 1200px; height: 1200px; overflow: hidden; background: var(--white); }
  .leaflet { position: relative; width: 1200px; height: 1200px; font-family: "Arimo", Arial, sans-serif; }
  .leaflet-title {
    position: absolute; left: 211px; top: 30px;
    font-family: "Nunito", "Arial Rounded MT Bold", sans-serif;
    font-weight: 900; font-size: 58px; letter-spacing: 0.5px; color: var(--teal);
  }
  .priority { position: absolute; left: 213px; width: 776px; height: 83px; }
  .priority svg { position: absolute; inset: 0; width: 776px; height: 83px; }
  .priority-num { font-family: "Nunito", "Arial Rounded MT Bold", sans-serif; font-weight: 900; font-size: 70px; }
  .priority-question {
    position: absolute; top: 0; height: 83px; display: flex; align-items: center;
    font-size: 15.5px; font-weight: 500; line-height: 20px;
  }
  .on-dark { color: var(--white); }
  .on-light { color: var(--teal-text); }
  .footer-note { position: absolute; left: 213px; top: 1085px; width: 180px; font-size: 13px; line-height: 16.5px; color: var(--navy); }
  .footer-thanks { position: absolute; left: 450px; top: 1085px; font-size: 13px; line-height: 16.5px; color: var(--navy); display: flex; gap: 5px; }
  .footer-thanks strong { font-weight: 700; }
  .footer-thanks ul { list-style: none; }
</style>
</head>
<body>
<main class="leaflet">
  <h1 class="leaflet-title">Our top 10 research priorities</h1>

  <section class="priority" style="top:105px">
    <svg viewBox="0 0 776 83"><path d="M72 0H776V83H71Q118 41 72 0Z" fill="var(--orange)"/><text class="priority-num" x="51" y="67" text-anchor="middle" fill="var(--orange)">1</text></svg>
    <p class="priority-question on-dark" style="left:106px;width:640px">What are the best ways to measure the outcome following lower limb orthopaedic surgery in children?</p>
  </section>

  <section class="priority" style="top:203px">
    <svg viewBox="0 0 776 83"><path d="M0 0H725Q680 20 682 83H0Z" fill="var(--lime)"/><text class="priority-num" x="725" y="74" text-anchor="middle" fill="var(--lime)">2</text></svg>
    <p class="priority-question on-light" style="left:38px;width:630px">Following orthopaedic surgery to the lower limbs, what should children’s rehabilitation include, how long is it expected to last and how does it affect the result of treatment?</p>
  </section>

  <section class="priority" style="top:301px">
    <svg viewBox="0 0 776 83"><path d="M103 0H776V83H55Q100 70 103 0Z" fill="var(--sage)"/><text class="priority-num" x="51" y="65" text-anchor="middle" fill="var(--sage)">3</text></svg>
    <p class="priority-question on-light" style="left:132px;width:600px">What is the short-term and long-term clinical and cost effectiveness of orthopaedic lower limb surgery (including best timing and technique) for children with Cerebral Palsy who can walk?</p>
  </section>

  <section class="priority" style="top:399px">
    <svg viewBox="0 0 776 83"><path d="M0 0H704Q680 30 685 83H0Z" fill="var(--teal)"/><text class="priority-num" x="719" y="67" text-anchor="middle" fill="var(--teal)">4</text></svg>
    <p class="priority-question on-dark" style="left:38px;width:620px">What are the short term and long term outcomes of surgery compared to non-surgical care in the treatment of Perthes disease of the hip?</p>
  </section>

  <section class="priority" style="top:497px">
    <svg viewBox="0 0 776 83"><path d="M117 0H776V83H59Q112 65 117 0Z" fill="var(--lime)"/><text class="priority-num" x="73" y="56" text-anchor="middle" fill="var(--lime)">5</text></svg>
    <p class="priority-question on-light" style="left:142px;width:600px">What is the clinical and cost effectiveness of pre-operative rehabilitation in children presenting with lower limb orthopaedic conditions?</p>
  </section>

  <section class="priority" style="top:595px">
    <svg viewBox="0 0 776 83"><path d="M0 0H682Q640 41 702 83H0Z" fill="var(--orange)"/><text class="priority-num" x="711" y="65" text-anchor="middle" fill="var(--orange)">6</text></svg>
    <p class="priority-question on-dark" style="left:38px;width:620px">What is the short-term and long-term clinical and cost effectiveness of Selective Dorsal Rhizotomy (SDR) in children with Cerebral Palsy who can walk?</p>
  </section>

  <section class="priority" style="top:694px">
    <svg viewBox="0 0 776 83"><path d="M114 0H776V83H95Q115 45 114 0Z" fill="var(--teal)"/><text class="priority-num" x="74" y="66" text-anchor="middle" fill="var(--teal)">7</text></svg>
    <p class="priority-question on-dark" style="left:132px;width:630px">Can surveillance and non-surgical treatment (e.g. physiotherapy, botulinum toxin injections, functional electrical stimulation, orthotics, casting) prevent the development of deformity requiring surgery in children with Cerebral Palsy?</p>
  </section>

  <section class="priority" style="top:792px">
    <svg viewBox="0 0 776 83"><path d="M0 0H776Q680 10 675 83H0Z" fill="var(--sage)"/><text class="priority-num" x="730" y="72" text-anchor="middle" fill="var(--sage)">8</text></svg>
    <p class="priority-question on-light" style="left:38px;width:590px">What is the best method of screening for Developmental Dysplasia of the Hip (DDH) in terms of clinical and cost effectiveness?</p>
  </section>

  <section class="priority" style="top:890px">
    <svg viewBox="0 0 776 83"><path d="M0 8Q100 15 105 83H776V0H0Z" fill="var(--lime)"/><path d="M0 0H776V8H0Z" fill="var(--lime)"/><path d="M0 8Q100 15 105 83H0Z" fill="var(--white)"/><text class="priority-num" x="50" y="78" text-anchor="middle" fill="var(--lime)">9</text></svg>
    <p class="priority-question on-light" style="left:198px;width:560px">What are the best strategies to optimise communication of information between patients/carers and clinicians in order to enable shared decision-making?</p>
  </section>

  <section class="priority" style="top:988px">
    <svg viewBox="0 0 776 83"><path d="M0 0H776V5Q620 0 622 83H0Z" fill="var(--orange)"/><text class="priority-num" x="707" y="79" text-anchor="middle" fill="var(--orange)">10</text></svg>
    <p class="priority-question on-dark" style="left:38px;width:500px">What is the best management for hip displacement in children with Cerebral Palsy?</p>
  </section>

  <p class="footer-note">Many thanks to all those people who helped us take this work off the ground and helped us finish it!</p>
  <div class="footer-thanks">
    <strong>Special thanks to:</strong>
    <ul>
      <li>The Northbrook Society of Young Bone Surgery</li>
      <li>The Calder Joint Surgeons Guild</li>
      <li>The University of Ashmere and the</li>
      <li>Harold Vane Collective, who always look for fair play in research!</li>
    </ul>
  </div>
</main>
</body>
</html>
```